Business Card Design Project

I need a new business card design for my Remodel/Design/Build company, Brightfield Renovation Works, Inc. See our website: www.brightfieldrenovationworks.com
We are an established company with a growing reputation and growing quickly. We are know for being on the forward edge of the industry, producing a great product and our "people friendly" approach.
I am looking for something cool, transitional, maybe even retro that captures the imagination, shows our sleek creativity and streamlined approach as well as communicates stability and trustworthiness.
Updates

Stainless steel business card design would be cool.

Please have all future designs with full logo colors and shown on a stainless steel business card.  Also, logo and tag line will most likely be printed with spot uv, so layers will be necessary.  Thank you.

Target Market(s)

30-65 yrs old, homeowners, appreciate fine things, median income $150+k, net worth $1+m

Industry/Entity Type

Business

Requirements
Must have
• Company Logo
Contact information
Website URL
Nice to have
• Tagline: Building Relationships and Remodeling Homes...One Client at a Time.
Double-sided okay.
Stainless steel business card.

```html
<!DOCTYPE html>
<html lang="en">
<head>
<meta charset="utf-8">
<title>Brightfield Renovation Works – Business Card</title>
<link rel="stylesheet" href="https://fonts.googleapis.com/css2?family=Ubuntu:wght@400;500;700&display=swap">
<style>
  :root {
    --page-bg: #d9dadc;
    --steel-light: #f4f5f6;
    --steel-mid: #c9cbce;
    --steel-dark: #8e9195;
    --brand-red: #a3161b;
    --ink: #1b1b1d;
    --ink-soft: #2a2b2e;
    --mark-circle: #8c1216;
  }
  * { box-sizing: border-box; margin: 0; padding: 0; }
  html, body {
    width: 1200px; height: 861px; overflow: hidden;
    background: var(--page-bg);
    font-family: "Ubuntu", Arial, sans-serif;
    color: var(--ink);
  }
  .sheet {
    position: relative; width: 1200px; height: 861px;
    display: flex; align-items: center; justify-content: center; gap: 40px;
  }
  .card {
    position: relative; width: 540px; height: 330px;
    border-radius: 18px; overflow: hidden;
    background:
      radial-gradient(circle at 22% 28%, rgba(255,255,255,.55) 0, rgba(255,255,255,0) 45%),
      repeating-radial-gradient(circle at 22% 28%, rgba(255,255,255,.12) 0 1px, rgba(0,0,0,.04) 1px 3px),
      conic-gradient(from 200deg at 22% 28%, var(--steel-light), var(--steel-dark) 12%, var(--steel-light) 28%, var(--steel-mid) 45%, var(--steel-light) 62%, var(--steel-dark) 78%, var(--steel-light));
    box-shadow: 0 12px 30px rgba(0,0,0,.25), inset 0 0 0 1px rgba(255,255,255,.6);
  }
  .brand {
    position: absolute; left: 28px; top: 26px;
    display: flex; align-items: center; gap: 14px;
  }
  .brand-dot {
    width: 74px; height: 74px; border-radius: 50%;
    background: var(--mark-circle);
  }
  .brand-name {
    color: var(--brand-red); font-weight: 500;
    font-size: 25px; line-height: 1.05; letter-spacing: 1.5px; text-transform: uppercase;
  }
  .tagline {
    position: absolute; right: 30px; bottom: 44px; text-align: right;
  }
  .tagline-main { font-weight: 700; font-size: 23px; line-height: 1.4; color: var(--ink); }
  .tagline-sub { font-size: 17px; margin-top: 8px; color: var(--ink); }
  .person { position: absolute; right: 30px; top: 116px; text-align: right; }
  .person-name { font-weight: 700; font-size: 29px; line-height: 1.15; color: var(--ink-soft); }
  .person-title { font-size: 15px; color: var(--ink); margin-top: 2px; }
  .contacts {
    position: absolute; right: 30px; bottom: 22px;
    list-style: none; text-align: right;
  }
  .contacts li {
    display: flex; justify-content: flex-end; align-items: center; gap: 7px;
    font-size: 14px; line-height: 17px; margin-top: 9px; color: var(--ink);
  }
  .contacts svg { width: 17px; height: 17px; flex: none; }
</style>
</head>
<body>
<main class="sheet">
  <section class="card card-front">
    <div class="brand">
      <span class="brand-dot"></span>
      <span class="brand-name">Brightfield<br>Renovation Works</span>
    </div>
    <div class="tagline">
      <p class="tagline-main">Building Relationships<br>and Remodeling Homes...</p>
      <p class="tagline-sub">One Client at a Time.</p>
    </div>
  </section>

  <section class="card card-back">
    <div class="brand">
      <span class="brand-dot"></span>
      <span class="brand-name">Brightfield<br>Renovation Works</span>
    </div>
    <div class="person">
      <p class="person-name">Dana Whitcombe</p>
      <p class="person-title">President</p>
    </div>
    <ul class="contacts">
      <li>555-014-2270
        <svg viewBox="0 0 20 20" aria-hidden="true"><circle cx="10" cy="10" r="9" fill="none" stroke="#1b1b1d" stroke-width="1.5"/><path d="M7 5h3l1 3-1.5 1a6 6 0 0 0 2.5 2.5L13 10l3 1v3a1 1 0 0 1-1 1A10 10 0 0 1 6 6a1 1 0 0 1 1-1z" fill="#1b1b1d" transform="scale(.8) translate(2.5 2.5)"/></svg>
      </li>
      <li>555-014-3575
        <svg viewBox="0 0 20 20" aria-hidden="true"><circle cx="10" cy="10" r="9" fill="none" stroke="#1b1b1d" stroke-width="1.5"/><rect x="7" y="4.5" width="6" height="11" rx="1.2" fill="#1b1b1d"/><rect x="8" y="6" width="4" height="6" fill="#f4f5f6"/></svg>
      </li>
      <li>dana@brightfieldrenovationworks.com
        <svg viewBox="0 0 20 20" aria-hidden="true"><circle cx="10" cy="10" r="9" fill="none" stroke="#1b1b1d" stroke-width="1.5"/><rect x="5" y="6.5" width="10" height="7" rx="1" fill="#1b1b1d"/><path d="M5.5 7l4.5 3.5L14.5 7" fill="none" stroke="#f4f5f6" stroke-width="1"/></svg>
      </li>
      <li>www.brightfieldrenovationworks.com
        <svg viewBox="0 0 20 20" aria-hidden="true"><circle cx="10" cy="10" r="9" fill="none" stroke="#1b1b1d" stroke-width="1.5"/><circle cx="10" cy="10" r="5" fill="none" stroke="#1b1b1d" stroke-width="1.2"/><ellipse cx="10" cy="10" rx="2.2" ry="5" fill="none" stroke="#1b1b1d" stroke-width="1"/><path d="M5 10h10" stroke="#1b1b1d" stroke-width="1"/></svg>
      </li>
    </ul>
  </section>
</main>
</body>
</html>
```